Business Card - Rebranding for Consulting Firm

We are renaming and rebranding our consulting firm and need to raise the level of quality of our cards as part of that effort. We consult to leading high tech, life science and other innovation sector companies.

Need a two-sided business card design.

Side 1: (a) Company logo (b) tag line: Maximize the Return on Your People (c) Name (d) Title (e) Phone 1: Office (f) Phone 2: Mobile (g) email: person@HollowmereAdvisory.com

Side 2: Two lines of text: (a) Vision is Essential. Markets are Moving. People Deliver Results. (b) We help you master all three.

Target Market(s)

Business and human resources executives and senior managers

Industry/Entity Type

Management Consulting

Contact Information for Business Card

Font styles to use
Sans Serif

Requirements
Must have
• clean, not too busy, but with a bit of creativity. Stick to the colors used in the attached logo
• appeal to high tech, life science companies
Nice to have
• prefer white background

```html
<!DOCTYPE html>
<html lang="en">
<head>
<meta charset="utf-8">
<title>Hollowmere Advisory – Stationery</title>
<link rel="stylesheet" href="https://fonts.googleapis.com/css2?family=Source+Sans+3:ital,wght@0,400;0,600;0,700;1,400&display=swap">
<style>
  :root{
    --backdrop:#55c1ec;
    --paper:#ffffff;
    --brand-dark:#1c5d99;
    --brand-light:#2a9ad6;
    --ink:#1e1e1e;
    --slate:#6f8794;
    --band-pale:#d3dbec;
    --band-mist:#d2e3ef;
    --rule:#c9cdd3;
  }
  *{box-sizing:border-box;margin:0;padding:0}
  html,body{width:1200px;height:1097px;overflow:hidden}
  body{background:var(--backdrop);font-family:"Source Sans 3",sans-serif;position:relative;color:var(--ink)}
  .sheet{position:absolute;background:var(--paper);box-shadow:0 6px 18px rgba(0,0,0,.18);overflow:hidden}

  .wordmark{display:flex;align-items:center;gap:8px;font-weight:600;color:var(--brand-dark);letter-spacing:-.5px;line-height:1}
  .wordmark .mark{background:var(--brand-dark);flex:none}
  .wordmark small{display:block;font-size:.28em;letter-spacing:.5em;font-weight:600;margin-top:3px}

  /* Letterhead */
  .letterhead{left:40px;top:134px;width:640px;height:828px}
  .letterhead .wordmark{position:absolute;left:44px;top:40px;font-size:40px}
  .letterhead .wordmark .mark{width:22px;height:22px}
  .letterhead .motto{position:absolute;left:44px;top:102px;font-style:italic;font-size:15px;line-height:1.35;color:var(--brand-dark)}
  .letterhead .band{position:absolute;left:0;bottom:140px;width:360px;height:120px}
  .letterhead .footer-rule{position:absolute;left:300px;right:0;bottom:118px;border-top:1px solid var(--rule)}
  .letterhead .contact{position:absolute;right:40px;bottom:24px;text-align:right;font-size:21px;line-height:1.35}
  .letterhead .contact .tagline{color:var(--brand-dark);font-size:23px}

  /* Business card */
  .card{width:440px;height:251px}
  .card-back{left:720px;top:134px;background:var(--slate)}
  .card-back .band{position:absolute;left:0;top:128px;width:170px;height:70px}
  .card-back .message{position:absolute;right:30px;top:70px;width:240px;color:#fff;font-size:13px;line-height:1.5;text-align:right}
  .card-back .message p+p{margin-top:8px}
  .card-front{left:720px;top:410px}
  .card-front .band{position:absolute;left:0;bottom:0;width:170px;height:80px}
  .card-front .wordmark{position:absolute;right:28px;top:34px;font-size:30px}
  .card-front .wordmark .mark{width:16px;height:16px}
  .card-front .person{position:absolute;right:28px;top:104px;text-align:right;font-size:13px;line-height:1.35}
  .card-front .person .name{color:var(--brand-light);font-weight:700;font-size:16px}
  .card-front .person .title{font-weight:600;margin-bottom:10px}
  .card-front .person .details{font-weight:600}

  /* Envelope */
  .envelope{left:720px;top:711px;width:440px;height:251px}
  .envelope .wordmark{position:absolute;left:26px;top:26px;font-size:28px}
  .envelope .wordmark .mark{width:15px;height:15px}
  .envelope .tagline{position:absolute;left:26px;top:70px;font-size:13px;font-weight:600}
  .envelope .band{position:absolute;left:0;top:150px;width:200px;height:101px}
</style>
</head>
<body>

<section class="sheet letterhead" aria-label="Letterhead">
  <div class="wordmark"><span class="mark"></span><div>Hollowmere<small>ADVISORY LLC</small></div></div>
  <div class="motto">
    <p>Vision is Essential. Markets are Moving. People Deliver Results.</p>
    <p>We help you master all three.</p>
  </div>
  <svg class="band" viewBox="0 0 360 120" aria-hidden="true">
    <rect x="0" y="0" width="360" height="6" fill="var(--band-pale)"/>
    <rect x="0" y="22" width="360" height="98" fill="var(--band-pale)"/>
  </svg>
  <div class="footer-rule"></div>
  <div class="contact">
    <p>Mobile: 555 010 2020</p>
    <p>person@HollowmereAdvisory.com</p>
    <p class="tagline">Maximize the Return on Your People</p>
  </div>
</section>

<section class="sheet card card-back" aria-label="Business card, back">
  <svg class="band" viewBox="0 0 170 70" aria-hidden="true">
    <rect x="0" y="0" width="170" height="4" fill="#fff"/>
    <rect x="0" y="16" width="170" height="54" fill="#fff" opacity=".85"/>
  </svg>
  <div class="message">
    <p>Vision is Essential. Markets are Moving. People Deliver Results.</p>
    <p>We help you master all three.</p>
  </div>
</section>

<section class="sheet card card-front" aria-label="Business card, front">
  <div class="wordmark"><span class="mark"></span><div>Hollowmere<small>ADVISORY LLC</small></div></div>
  <div class="person">
    <p class="name">Your Name</p>
    <p class="title">Your Title</p>
    <div class="details">
      <p>Office: 555 010 1010</p>
      <p>Mobile: 555 010 2020</p>
      <p>person@HollowmereAdvisory.com</p>
    </div>
  </div>
  <svg class="band" viewBox="0 0 170 80" aria-hidden="true">
    <rect x="0" y="0" width="170" height="4" fill="var(--slate)"/>
    <rect x="0" y="16" width="60" height="64" fill="var(--brand-light)"/>
    <rect x="60" y="16" width="110" height="64" fill="var(--brand-dark)"/>
  </svg>
</section>

<section class="sheet envelope" aria-label="Envelope">
  <div class="wordmark"><span class="mark"></span><div>Hollowmere<small>ADVISORY LLC</small></div></div>
  <p class="tagline">Maximize the Return on Your People</p>
  <svg class="band" viewBox="0 0 200 101" aria-hidden="true">
    <rect x="0" y="0" width="200" height="5" fill="var(--band-mist)"/>
    <rect x="0" y="18" width="200" height="83" fill="var(--band-mist)"/>
  </svg>
</section>

</body>
</html>
```